Walking in Grace book cover

Needing a book cover design and I have attached 3 sample covers for a starting point. I would like the design to use similar font as the sample cover along with a red and white theme. I would like a background image of broken shackles. On the back cover leave room for the author's bio and picture. The front cover and book details are below:
Book size: 6x9 or. 4.5x7
Title: Walking in Grace
Subtitle: Standing Firm Against Every Snare Through Scripture
Author: Marlon Petway
No spine is needed for the book due to it is a smaller book and the text will not fit. Yes, we are looking at every design and will choose winner on or before 4/20/2022

```html
<!DOCTYPE html>
<html lang="en">
<head>
<meta charset="utf-8">
<title>Walking in Grace — Book Cover</title>
<link href="https://fonts.googleapis.com/css2?family=Marcellus&display=swap" rel="stylesheet">
<style>
  :root {
    --sky-white: #fbfdff;
    --sky-blue: #d3e2f3;
    --title-red: #e8232a;
    --ink: #111111;
    --steel-light: #b9bcc0;
    --steel-dark: #5d6166;
  }
  html, body {
    margin: 0;
    padding: 0;
    width: 800px;
    height: 1200px;
    overflow: hidden;
  }
  .cover {
    position: relative;
    width: 800px;
    height: 1200px;
    overflow: hidden;
    font-family: "Marcellus", "Optima", sans-serif;
  }
  .cover__sky {
    position: absolute;
    inset: 0;
    background:
      radial-gradient(ellipse at 20% 15%, var(--sky-blue) 0%, transparent 45%),
      radial-gradient(ellipse at 85% 30%, var(--sky-blue) 0%, transparent 40%),
      radial-gradient(ellipse at 10% 75%, var(--sky-blue) 0%, transparent 40%),
      radial-gradient(ellipse at 75% 92%, var(--sky-blue) 0%, transparent 45%),
      var(--sky-white);
  }
  .shackle {
    position: absolute;
    border-radius: 40px;
    background: linear-gradient(135deg, var(--steel-light), var(--steel-dark));
    opacity: 0.55;
  }
  .shackle--upper {
    left: 80px;
    top: 34px;
    width: 330px;
    height: 290px;
  }
  .shackle--lower {
    left: 436px;
    top: 808px;
    width: 330px;
    height: 292px;
  }
  .author {
    position: absolute;
    left: 440px;
    top: 318px;
    margin: 0;
    font-size: 44px;
    font-weight: 400;
    color: var(--ink);
    letter-spacing: 0.5px;
    white-space: nowrap;
  }
  .title {
    position: absolute;
    left: 0;
    top: 392px;
    width: 800px;
    margin: 0;
    text-align: center;
    font-size: 120px;
    font-weight: 400;
    line-height: 130px;
    color: var(--title-red);
    text-transform: uppercase;
  }
  .title span { display: block; }
  .subtitle {
    position: absolute;
    left: 44px;
    top: 822px;
    margin: 0;
    font-size: 31px;
    line-height: 42px;
    font-weight: 400;
    color: var(--ink);
  }
  .subtitle span { display: block; }
</style>
</head>
<body>
  <main class="cover">
    <div class="cover__sky" role="img" aria-label="Soft white and pale blue cloudy sky background"></div>
    <div class="shackle shackle--upper" role="img" aria-label="Open iron shackle with a broken chain"></div>
    <div class="shackle shackle--lower" role="img" aria-label="Open iron shackle with a broken chain"></div>

    <p class="author">Marlon Petway</p>
    <h1 class="title"><span>Walking</span><span>in</span><span>Grace</span></h1>
    <p class="subtitle"><span>Standing Firm Against</span><span>Every Snare Through</span><span>Scripture</span></p>
  </main>
</body>
</html>
```